Homepage layout for online ad network

Attached is our Valtry Media logo and updated brief (I can't seem to delete the old logo and brief, but they're no longer relevant).

This project was originally posted with a different logo and corporate name, but we have decided to stay with our current logo and name and redesign the site.

Your design is for a homepage only - design, no coding (I'll get someone else to take your PSD and code it).

Your homepage will make use of a Flash slider - BUT YOU ARE NOT REQUIRED TO PROVIDE THE FLASH. Instead, simply provide the layout and at least two static examples out of the four different sections that will eventually be in the slider.

Much of this design is based on the design of a competitor (listed in the brief).

Please ask whatever questions you need to in order to clarify instructions.
Updates

Project updated to include new logo (and correspondingly new color scheme).

Brief changed slightly.

Thank you for submitting designs for this project in the past.

After some internal strategy work, we have decided to retain our initial corporate identity, Valtry Media.

If you have submitted a design for the original brief and are available, please re-work your best prior design to reflect the color scheme in the newly uploaded logo.

Target Market(s)

This site is aimed primarily at young professionals who buy digital media on behalf of large advertisers.

Industry/Entity Type

Media

Requirements
Must have
• modern white space
Should not have
• no Flash outside of slider

```html
<!DOCTYPE html>
<html lang="en">
<head>
<meta charset="utf-8">
<title>Valtry Media — Home</title>
<link href="https://fonts.googleapis.com/css2?family=Arimo:ital,wght@0,400;0,700;1,700&family=Teko:wght@400;500&family=Roboto+Condensed:wght@700&display=swap" rel="stylesheet">
<style>
:root{
  --ink:#000;
  --page:#161616;
  --red:#b5000c;
  --red-dark:#5e0006;
  --red-text:#d4101c;
  --white:#fff;
  --grey-text:#555;
  --brand-text:#333;
  --panel-top:#8a8a8a;
  --panel-bot:#3e3e3e;
  --teal:#0d3048;
  --card:#1b1b1b;
}
*{box-sizing:border-box;margin:0;padding:0}
html,body{width:1200px;height:900px;overflow:hidden}
body{position:relative;background:var(--page);font-family:"Arimo",Arial,sans-serif;color:var(--white)}
.top-strip{position:absolute;left:0;top:0;width:1200px;height:108px;background:linear-gradient(180deg,#2b2b2b,#161616)}
.preview-note{position:absolute;left:600px;top:0;width:600px;height:46px;background:var(--white);color:var(--ink);font:italic 700 28px "Arimo",Arial,sans-serif;letter-spacing:-.5px;padding:7px 0 0 40px}
.brand-tab{position:absolute;left:96px;top:-6px;width:252px;height:124px;background:var(--white);border-radius:0 0 12px 12px;box-shadow:0 3px 6px rgba(0,0,0,.6);z-index:3}
.brand-mark{position:absolute;left:20px;top:28px;width:44px;height:44px;background:var(--red)}
.brand-name{position:absolute;left:84px;top:33px;width:160px;font:400 27px/29px "Arimo",Arial,sans-serif;letter-spacing:3px;color:var(--brand-text)}
.brand-tag{position:absolute;left:22px;top:95px;width:210px;font-size:11px;color:var(--brand-text);text-align:center}
.red-bar{position:absolute;left:0;width:1200px;background:linear-gradient(180deg,#c20010 0%,#8c0009 55%,var(--red-dark) 100%);border-top:1px solid #e0303a}
.red-bar.upper{top:108px;height:37px}
.red-bar.lower{top:416px;height:36px}
.main-nav{position:absolute;right:139px;top:10px;font:700 14px "Arimo",Arial,sans-serif;display:flex;gap:8px}
.main-nav span.sep{font-weight:400}
.hero{position:absolute;left:0;top:145px;width:1200px;height:271px;background:linear-gradient(180deg,#9a9a9a 0%,#d9d9d9 40%,#f7f7f7 100%)}
.hero-photo{position:absolute;left:95px;top:125px;width:365px;height:291px;background:linear-gradient(160deg,#3a3a3a,#1a1a1a 60%,#e8e8e8);border-radius:4px;z-index:2}
.hero-title{position:absolute;left:495px;top:76px;font:400 98px/1 "Arimo",Arial,sans-serif;color:var(--ink)}
.hero-note{position:absolute;left:510px;top:179px;font-size:11px;color:var(--grey-text);letter-spacing:.3px}
.about{position:absolute;left:118px;top:497px;width:640px}
.about h1{font:400 29px "Arimo",Arial,sans-serif;margin-bottom:4px}
.about p{font-size:12px;line-height:17px;margin-bottom:17px;letter-spacing:-.1px}
.btn-more{position:absolute;display:block;width:75px;height:20px;background:linear-gradient(180deg,#e4202c,#9a0008);border:1px solid #ff5a62;font:700 9px/18px "Roboto Condensed",Arial,sans-serif;text-align:center;letter-spacing:.6px;box-shadow:1px 1px 2px #000}
.rule{position:absolute;left:105px;top:722px;width:665px;height:1px;background:#555}
.category{position:absolute;top:744px;width:155px}
.category h2{font:400 31px/1 "Teko",sans-serif;letter-spacing:2px;text-align:center;color:var(--red-text);height:38px}
.category.beauty h2{color:var(--white)}
.cat-card{background:var(--card);border:1px solid #777;height:140px;padding:9px 9px 0 9px}
.cat-thumb{height:59px;background:linear-gradient(135deg,#8a8a8a,#3a3a3a)}
.beauty .cat-thumb{background:linear-gradient(135deg,#6e8f3a,#e6c48a)}
.cat-card h3{font:700 11px "Arimo",Arial,sans-serif;color:var(--red-text);margin:8px 0 8px 6px}
.cat-card p{font-size:9.5px;line-height:11px;margin-left:6px}
.news{position:absolute;left:782px;top:495px;width:294px;height:420px;border-radius:10px;background:linear-gradient(180deg,var(--panel-top),var(--panel-bot));border:1px solid #999;box-shadow:0 0 8px #000}
.news-head{position:absolute;left:20px;top:14px;display:flex;align-items:center;gap:8px;font-size:18px}
.news-date{position:absolute;left:13px;top:50px;width:267px;height:34px;background:var(--teal);border:1px solid #5a6c7a;font:700 13px/32px "Roboto Condensed",Arial,sans-serif;display:flex;justify-content:space-between;padding:0 18px 0 26px}
.news-item{position:absolute;left:24px;width:255px}
.news-item h4{font:700 13px "Arimo",Arial,sans-serif;text-decoration:underline;display:flex;align-items:center;gap:6px;margin-bottom:5px}
.news-item p{font-size:12px;line-height:19px;color:var(--white)}
</style>
</head>
<body>
<div class="top-strip"></div>
<div class="preview-note">LINK FOR FULL PREVIEW IN COMMENT</div>

<header class="brand-tab">
  <span class="brand-mark"></span>
  <div class="brand-name">VALTRY<br>MEDIA</div>
  <div class="brand-tag">every campaign finds its people</div>
</header>

<div class="red-bar upper">
  <nav class="main-nav"><span>Beauty</span><span class="sep">|</span><span>Cooking</span><span class="sep">|</span><span>Parenting</span><span class="sep">|</span><span>Video</span></nav>
</div>

<section class="hero">
  <div class="hero-title">WELCOME</div>
  <div class="hero-note">*all gray area can be flash movie, browser wide. With or without top meni in red bar.</div>
</section>
<div class="hero-photo" role="img" aria-label="Magician in a tuxedo holding a wand and top hat"></div>

<div class="red-bar lower"></div>

<section class="about">
  <h1>Who we are ?</h1>
  <p><b>turpis. Sed tristique. Integer nulla nisl, dapibus et, interdum vel,</b> sollicitudin in, dui. Nullam venatis, augue at viverra egestas, lacus neque molestie metus, eu tincidunt ipsum nisi vitae tellus.</p>
  <p>Nullam eget nulla. Phasellus id dolor. Mauris molestie. Aliquam vitae felis in pede congue auctor. Phaselluut pede id orci aliquam adipiscing. Sed dolor dui, dapibus quis, nonummy non, gravidarton sollicitudin, mauris. Nam cursus. Integer lobortis, est at rhoncus auctor, tortor odio hendrerit orci, non malesuada nisl ipsum in nunc. Curabitur arcu justo, euismod vel, tempor eget, volutpatoncupat tincidunt, odio.</p>
</section>
<a class="btn-more" style="left:666px;top:670px">READ MORE</a>

<div class="rule"></div>

<article class="category beauty" style="left:106px">
  <h2>BEAUTY</h2>
  <div class="cat-card"><div class="cat-thumb" role="img" aria-label="Smiling woman outdoors"></div><h3>Cras lacinia nunc in</h3><p>Bandit aenean commodo vulputate ante proin</p></div>
</article>
<article class="category" style="left:274px">
  <h2>COOKING</h2>
  <div class="cat-card"><div class="cat-thumb" role="img" aria-label="Hands preparing food"></div><h3>Ad litora torquent</h3><p>Faucibus odio sit ametue maecenas</p></div>
</article>
<article class="category" style="left:442px">
  <h2>PARENTING</h2>
  <div class="cat-card"><div class="cat-thumb" role="img" aria-label="Parent with a baby"></div><h3>Maecenas eu</h3><p>Bandit aenean commodo vulputate ante proin</p></div>
</article>
<article class="category" style="left:609px">
  <h2>VIDEO</h2>
  <div class="cat-card"><div class="cat-thumb" role="img" aria-label="Film clapperboard and actress"></div><h3>Sapien egestas conval</h3><p>Hendrerit turpis non lacus praesent convallis</p></div>
</article>

<aside class="news">
  <div class="news-head">
    <svg width="32" height="26" viewBox="0 0 32 26" aria-hidden="true"><rect x="2" y="3" width="26" height="20" rx="2" fill="#eee" stroke="#999"/><rect x="6" y="7" width="9" height="7" fill="#aaa"/><path d="M18 8h7M18 11h7M6 17h19M6 20h19" stroke="#888"/></svg>
    <span>Latest News</span>
  </div>
  <div class="news-date"><span>ON 12 OCTOBER 2010</span><span>London</span></div>

  <div class="news-item" style="top:98px">
    <h4><svg width="11" height="11" viewBox="0 0 11 11" aria-hidden="true"><rect width="11" height="11" fill="#ddd"/><path d="M2 5.5h6M5 2.5l3 3-3 3" stroke="#333" fill="none" stroke-width="1.4"/></svg>Lorem ipsum dolor sit amet</h4>
    <p>varius vitae, orci. Donec arcu elit, placerat ac, pulvinar et, lacinia eu, risus.</p>
  </div>
  <a class="btn-more" style="left:200px;top:161px">READ MORE</a>

  <div class="news-item" style="top:190px">
    <h4><svg width="11" height="11" viewBox="0 0 11 11" aria-hidden="true"><rect width="11" height="11" fill="#ddd"/><path d="M2 5.5h6M5 2.5l3 3-3 3" stroke="#333" fill="none" stroke-width="1.4"/></svg>Lorem ipsum dolor sit amet</h4>
    <p>blandit dui. Proin elit lorem, blandit id, volutpat vel, facilisis sed, enim. Aenean nonummy volutpat eros.</p>
  </div>
  <a class="btn-more" style="left:200px;top:267px">READ MORE</a>

  <div class="news-item" style="top:296px">
    <h4><svg width="11" height="11" viewBox="0 0 11 11" aria-hidden="true"><rect width="11" height="11" fill="#ddd"/><path d="M2 5.5h6M5 2.5l3 3-3 3" stroke="#333" fill="none" stroke-width="1.4"/></svg>Convallis pellentesque uspendisse</h4>
    <p>varius vitae, orci. Donec arcu elit, placerat ac, pulvinar et, lacinia eu, risus. Quisque rhoncus ultrices lorem. Fusce facilisis, sem vitae condimentum</p>
  </div>
  <a class="btn-more" style="left:200px;top:391px">READ MORE</a>
</aside>
</body>
</html>
```